Restaurant menu design

I need a menu for a restaurant in Spain.
It has to be bohemian but modern. We need something romantic and elegant.
The restaurant is elegant with good food and an excellent reputation. It is also modern at the same time.
The restaurant is superbly decorated and very chick so we need something "class" to fit in with the surroundings.
The size of the document must be 325 mm in high and 245 mm as a maximum and preferably made in indesign.

Reason: Thank you all for your designs.
So far all your designs are ok but it isn´t what we are looking for. Most of the designs are too loaded, too many colors and too much decoration.

Target Market(s)

Adults of various age groups and different nationalities mostly European.

Industry/Entity Type

Restaurant

Requirements
Must have
• The menu must have two interior pages with the text as in the document attached.It must be easily legible.
Nice to have
• See what kind of menus they use in important restaurants in places like Paris, see what designs are in trend, but Not necessarily doing the same style if it doesn’t fit in with the description above.
Should not have
• Nothing old fashioned.

```html
<!DOCTYPE html>
<html lang="es">
<head>
<meta charset="utf-8">
<title>La Lumière — Carnes y Postres</title>
<link href="https://fonts.googleapis.com/css2?family=Source+Sans+3:wght@300;400&display=swap" rel="stylesheet">
<style>
  :root {
    --paper: #ffffff;
    --band-light: #c9a297;
    --band-dark: #b08a7e;
    --plum: #8e5e84;
    --ink: #1f1a1c;
  }
  html, body { margin: 0; padding: 0; overflow: hidden; }
  body { width: 904px; height: 1200px; background: var(--paper); }
  .menu-page {
    position: relative; width: 904px; height: 1200px; overflow: hidden;
    background: var(--paper); font-family: "Source Sans 3", sans-serif; color: var(--ink);
  }
  .side-band { position: absolute; top: 0; left: 0; width: 111px; height: 100%; background: var(--band-light); }
  .side-band-edge { position: absolute; top: 0; left: 111px; width: 18px; height: 100%; background: var(--band-dark); }

  .section-title {
    position: absolute; margin: 0; font-weight: 300; color: var(--plum);
    letter-spacing: 0.5px; line-height: 1;
  }
  .title-meats { left: 210px; top: 82px; font-size: 50px; }
  .title-desserts { left: 213px; top: 728px; font-size: 52px; }

  .dish-list { position: absolute; margin: 0; padding: 0; list-style: none; font-size: 16px; }
  .dish {
    display: grid; align-items: end; line-height: 22px; margin-bottom: 10.6px;
  }
  .meats { left: 212px; top: 148px; }
  .meats .dish { grid-template-columns: 515px 90px; }
  .desserts { left: 219px; top: 798px; }
  .desserts .dish { grid-template-columns: 523px 90px; margin-bottom: 11px; }
  .dish-price { white-space: nowrap; }

  .sauce-box {
    position: absolute; left: 212px; top: 620px; width: 612px; height: 62px;
    border: 1.3px solid var(--ink); box-sizing: border-box; padding: 8px 10px 0;
  }
  .sauce-label { color: var(--plum); font-size: 17px; line-height: 20px; margin: 0; }
  .sauce-list {
    display: flex; justify-content: space-between; margin: 5px 0 0; padding: 0;
    list-style: none; font-size: 12.5px; white-space: nowrap;
  }
  .sauce-list .dot { padding: 0 4px; }

  .brand-name {
    position: absolute; right: 22px; top: 1124px; font-size: 20px; font-weight: 400;
    color: var(--plum); line-height: 1;
  }
</style>
</head>
<body>
<main class="menu-page">
  <div class="side-band"></div>
  <div class="side-band-edge"></div>

  <h2 class="section-title title-meats">Carnes</h2>
  <ul class="dish-list meats">
    <li class="dish"><span>Pechuga de Pollo “Marie France” con Champiñones y Bacon.</span><span class="dish-price">11,95 €</span></li>
    <li class="dish"><span>Chuletas de Cordero.</span><span class="dish-price">14,50 €</span></li>
    <li class="dish"><span>Costillas de Cerdo con Salsa Barbacoa.</span><span class="dish-price">9,95 €</span></li>
    <li class="dish"><span>Paletilla de Cordero Lechal.</span><span class="dish-price">19,75 €</span></li>
    <li class="dish"><span>Le Strogonoff. Finas tiras de Solomillo con su Salsa de Champiñones.</span><span class="dish-price">15,90 €</span></li>
    <li class="dish"><span>Solomillo de Ternera.</span><span class="dish-price">18,50 €</span></li>
    <li class="dish"><span>Solomillo de Ternera a la Ibérica con Jamón Ibérico y Ligera Salsa<br>de Vino Tinto.</span><span class="dish-price">20,75 €</span></li>
    <li class="dish"><span>“Hamburger Maison Steak Hachè”. Picata de Solomillo de Ternera,<br>Huevo Frito y Patatas Fritas</span><span class="dish-price">14,50 €</span></li>
    <li class="dish"><span>Solomillo de Cerdo al Horno con Bacon y su Salsa de Setas.</span><span class="dish-price">14,25 €</span></li>
    <li class="dish"><span>Entrecôte de Ternera.</span><span class="dish-price">14,75 €</span></li>
    <li class="dish"><span>T-Bone Steak de Ternera.</span><span class="dish-price">16,75 €</span></li>
    <li class="dish"><span>Chuletón de Ternera.</span><span class="dish-price">20,25 €</span></li>
    <li class="dish"><span>Parrillada de Carnes y Embutidos.</span><span class="dish-price">21,50 €</span></li>
  </ul>

  <section class="sauce-box">
    <p class="sauce-label">Salsas:</p>
    <ul class="sauce-list">
      <li>Pimienta.&nbsp;&nbsp;&nbsp;2,85 €</li><li class="dot">·</li>
      <li>Roquefort.&nbsp;&nbsp;&nbsp;2,95 €</li><li class="dot">·</li>
      <li>Bearnaise.&nbsp;&nbsp;&nbsp;2,95 €</li><li class="dot">·</li>
      <li>de Champiñones.&nbsp;&nbsp;2,65 €</li>
    </ul>
  </section>

  <h2 class="section-title title-desserts">Los Postres de la Lumière</h2>
  <ul class="dish-list desserts">
    <li class="dish"><span>Frambuesas “La Lumière”.</span><span class="dish-price">6,25 €</span></li>
    <li class="dish"><span>Cocktail de Frutas Exóticas.</span><span class="dish-price">5,25 €</span></li>
    <li class="dish"><span>Sorbete de Limón, Coulis de Fresa y Vodka.</span><span class="dish-price">5,50 €</span></li>
    <li class="dish"><span>Pastel de Chocolate Casero con su Salsa de Vainilla.</span><span class="dish-price">6,25 €</span></li>
    <li class="dish"><span>Crême Brulée.</span><span class="dish-price">6,25 €</span></li>
    <li class="dish"><span>Tarta de Manzana Casera “Tatín” y su Helado de Vainilla.</span><span class="dish-price">6,95 €</span></li>
    <li class="dish"><span>Copa Glacier Nord.</span><span class="dish-price">6,75 €</span></li>
    <li class="dish"><span>Pera al Chocolate Caliente y Helado de Macadamia.</span><span class="dish-price">5,95 €</span></li>
    <li class="dish"><span>Tarta de Queso con Coulis de Fresa.</span><span class="dish-price">5,75 €</span></li>
    <li class="dish"><span>Nuestra Mousse de Chocolate.</span><span class="dish-price">5,75 €</span></li>
  </ul>

  <div class="brand-name">La Lumière</div>
</main>
</body>
</html>
```